Hi,

I would like to have a invitation made for a party. exactly like the picture in the link below.

http://pinboardia.example/pin/730215948361027459/

However, Please change the colors into fun/ girly feeling. font can be different and size of the card should be the same

Name of the girl: RINA
What: Bachelorette Party
Where:TOLO Boat
Dubai Coral Quay Sailing Club
When:7th of February 2013

No RSVP required. (so no need to put it)

```html
<!DOCTYPE html>
<html lang="en">
<head>
<meta charset="utf-8">
<title>Rina's Bachelorette Invitation</title>
<link rel="stylesheet" href="https://fonts.googleapis.com/css2?family=Pinyon+Script&family=Carlito&family=Smythe&display=swap">
<style>
  :root {
    --page: #ffffff;
    --paper: #fffafc;
    --ink: #2d0a28;
    --rule: #4a1a40;
    --hot-pink: #e6248a;
    --bubblegum: #ff8fc7;
    --blush: #ffd3e8;
    --blush-faint: #ffe8f2;
  }
  * { box-sizing: border-box; margin: 0; padding: 0; }
  html, body {
    width: 1200px; height: 762px; overflow: hidden;
    background: var(--page);
  }
  .canvas { position: relative; width: 1200px; height: 762px; }

  .card {
    position: absolute; left: 65px; top: 51px;
    width: 1068px; height: 634px;
    border: 1.5px solid var(--rule);
    background: var(--paper);
    overflow: hidden;
  }
  .panel-divider {
    position: absolute; top: 0; bottom: 0; width: 1.5px;
    background: var(--rule);
  }
  .panel-divider--first { left: 355px; }
  .panel-divider--second { left: 711px; }

  .ornament-band {
    position: absolute; left: 0; right: 0; height: 44px;
    background: var(--blush);
  }
  .ornament-band--top { top: 20px; }
  .ornament-band--bottom { top: 562px; }

  .damask-watermark {
    position: absolute; left: 273px; top: 69px;
    width: 425px; height: 371px;
    border-radius: 50% 50% 38% 38%;
    background: var(--blush-faint);
  }

  .ornament-small {
    position: absolute;
    border-radius: 50% 50% 40% 40%;
    background: var(--bubblegum);
  }
  .ornament-small--single { left: 146px; top: 305px; width: 48px; height: 44px; }
  .ornament-small--invite { left: 865px; top: 113px; width: 46px; height: 50px; }

  .guest-name {
    position: absolute; left: 12px; top: 92px;
    font-family: "Pinyon Script", cursive;
    font-weight: 400;
    font-size: 104px; line-height: 1;
    color: var(--ink);
  }
  .tagline {
    position: absolute; top: 220px;
    font-family: "Carlito", sans-serif;
    font-size: 42px; line-height: 42px;
    color: var(--ink); white-space: nowrap;
  }
  .tagline--first { left: 36px; }
  .tagline--second { left: 371px; }

  .headline {
    position: absolute; left: 0; top: 0;
    width: 1068px; height: 634px;
  }
  .headline text {
    font-family: "Smythe", serif;
    fill: var(--hot-pink);
  }

  .details-frame {
    position: absolute; left: 758px; top: 140px;
    width: 262px; height: 356px;
    border: 2px solid var(--bubblegum);
    border-radius: 9px;
    background: var(--paper);
    text-align: center;
    color: var(--ink);
  }
  .invite-title {
    margin-top: 52px;
    font-family: "Smythe", serif;
    font-weight: 400;
    font-size: 42px; line-height: 1;
    text-transform: uppercase;
    color: var(--hot-pink);
  }
  .event-details {
    margin-top: 30px;
    font-family: "Carlito", sans-serif;
    font-size: 17.5px; line-height: 22px;
  }
  .event-details dt { margin-top: 22px; }
  .event-details dt:first-child { margin-top: 0; }
</style>
</head>
<body>
<div class="canvas">
  <section class="card" aria-label="Bachelorette party invitation">
    <div class="damask-watermark" role="img" aria-label="Large faint pink damask motif behind the centre panel"></div>
    <div class="ornament-band ornament-band--top" role="img" aria-label="Pink scrollwork border along the top edge"></div>
    <div class="ornament-band ornament-band--bottom" role="img" aria-label="Pink scrollwork border along the bottom edge"></div>

    <div class="panel-divider panel-divider--first"></div>
    <div class="panel-divider panel-divider--second"></div>

    <h1 class="guest-name">Rina’s</h1>
    <p class="tagline tagline--first">LAST CHANCE TO</p>
    <p class="tagline tagline--second">CELEBRATE BEING</p>

    <svg class="headline" viewBox="0 0 1068 634" role="img" aria-label="Single">
      <text x="28" y="532" font-size="330" textLength="71" lengthAdjust="spacingAndGlyphs">S</text>
      <text x="110" y="532" font-size="250" textLength="212" lengthAdjust="spacingAndGlyphs">IN</text>
      <text x="382" y="532" font-size="250" textLength="305" lengthAdjust="spacingAndGlyphs">GLE</text>
    </svg>
    <div class="ornament-small ornament-small--single" role="img" aria-label="Small pink damask ornament"></div>

    <div class="details-frame">
      <h2 class="invite-title">Your<br>Invited</h2>
      <dl class="event-details">
        <dt>Where:</dt>
        <dd>TOLO Boat<br>Dubai Coral Quay Sailing Club</dd>
        <dt>When:</dt>
        <dd>7th of February 2013</dd>
      </dl>
    </div>
    <div class="ornament-small ornament-small--invite" role="img" aria-label="Small pink damask ornament"></div>
  </section>
</div>
</body>
</html>
```